Upland Bird Hunting Preserve and Pointing Dog kennel

Need Price packages outlined for the bird hunting business. List the kennel and that we provide training and dogs for sale.
The preserve is "Tall Heron Expeditions" the dog kennel is "Pine Hollow Setters"
1/2 Day Upland Field Hunts: 5 Pheasants $120
7 Chukar $125
Continental Hunt 12 Pheasants $325 includes meal, minimum 12 hunters
Guides available $100

Target Market(s)

upland bird hunters

Industry/Entity Type

hunting, outdoor

Colors
EE7325
F08F49
F5BC92
FAE3D3
FDF4ED

```html
<!DOCTYPE html>
<html lang="en">
<head>
<meta charset="utf-8">
<title>Tall Heron Expeditions – Hunting Packages</title>
<link rel="stylesheet" href="https://fonts.googleapis.com/css2?family=Poppins:wght@300;400;500;600;700;800;900&display=swap">
<style>
  :root {
    --orange: #EE7325;
    --orange-light: #F08F49;
    --peach: #F5BC92;
    --cream: #FAE3D3;
    --ivory: #FDF4ED;
    --bark-dark: #140b06;
    --bark: #2b1609;
    --rust: #7a3712;
    --rust-deep: #4a200a;
    --stage: #d6d4d1;
    --white: #ffffff;
  }
  * { box-sizing: border-box; margin: 0; padding: 0; }
  html, body {
    width: 1200px; height: 800px; overflow: hidden;
    background: var(--stage);
    font-family: "Poppins", sans-serif;
  }
  .poster {
    position: absolute; left: 331px; top: 20px;
    width: 538px; height: 760px; overflow: hidden;
    background:
      radial-gradient(ellipse at 50% 60%, #3d2110 0%, var(--bark) 45%, var(--bark-dark) 100%);
    color: var(--white);
  }
  .line { position: absolute; left: 0; width: 100%; text-align: center; line-height: 1; white-space: nowrap; }
  .hero-photo {
    position: absolute; left: 0; top: 40px; width: 100%; height: 330px;
    background:
      radial-gradient(ellipse at 62% 55%, rgba(240,143,73,.85) 0%, rgba(180,100,40,.55) 25%, transparent 55%),
      linear-gradient(180deg, var(--bark-dark) 0%, #6f7a3a 25%, #8d8f45 40%, #8a5a25 70%, var(--bark) 100%);
  }
  .brand-name { top: 17px; font-size: 33px; font-weight: 900; letter-spacing: -.5px; text-shadow: 0 2px 4px rgba(0,0,0,.6); }
  .brand-sub { top: 51px; font-size: 26px; font-weight: 700; text-shadow: 0 2px 4px rgba(0,0,0,.6); }
  .brand-tag { top: 79px; font-size: 13px; font-weight: 600; color: var(--orange); }
  .package-banner {
    position: absolute; left: 20px; top: 285px; width: 497px; height: 71px;
    background: linear-gradient(90deg, var(--rust-deep) 0%, var(--rust) 35%, #8c4216 60%, var(--rust-deep) 100%);
    border-radius: 4px; box-shadow: 0 4px 10px rgba(0,0,0,.5);
  }
  .banner-title { top: 289px; font-size: 37px; font-weight: 800; letter-spacing: -.5px; text-shadow: 0 2px 3px rgba(0,0,0,.5); }
  .banner-sub { top: 325px; font-size: 24px; font-weight: 800; color: var(--orange); }
  .glow-rule { position: absolute; left: 40px; width: 458px; height: 2px;
    background: linear-gradient(90deg, transparent, var(--ivory), transparent); }
  .price-col { position: absolute; top: 370px; width: 166px; text-align: center; line-height: 1; }
  .price-col .bird { font-size: 18px; font-weight: 300; color: var(--cream); }
  .price-col .price { margin-top: 6px; font-size: 26px; font-weight: 800; color: var(--orange); }
  .col-divider { position: absolute; top: 364px; width: 1px; height: 68px; background: var(--orange); }
  .guide-line { top: 456px; font-size: 21px; font-weight: 600; }
  .guide-line .amount { color: var(--orange); font-weight: 800; }
  .guide-line .unit { font-weight: 500; }
  .section-title { font-weight: 700; color: var(--orange); }
  .continental { top: 501px; font-size: 26px; }
  .minimum { top: 530px; font-size: 14px; font-weight: 600; }
  .fine { font-size: 10.5px; font-weight: 400; color: var(--ivory); }
  .fine-1 { top: 546px; }
  .fine-2 { top: 559px; }
  .turkey { top: 588px; font-size: 19px; }
  .detail { font-size: 13px; font-weight: 400; color: var(--cream); }
  .detail-1 { top: 612px; }
  .detail-2 { top: 627px; }
  .detail-3 { top: 642px; }
  .kennel-note { position: absolute; left: 21px; top: 684px; font-size: 17.5px; font-weight: 700; line-height: 1; white-space: nowrap; }
  .contact-tag { position: absolute; top: 714px; height: 26px; }
  .contact-tag .tag-frame { position: absolute; left: 0; top: 0; }
  .contact-tag span { position: relative; display: flex; align-items: center; justify-content: center; height: 26px; gap: 7px; line-height: 1; }
  .contact-name { left: 20px; width: 121px; }
  .contact-name span { font-size: 12.5px; font-weight: 400; color: var(--cream); }
  .contact-phone { left: 136px; width: 168px; }
  .contact-phone span { font-size: 16px; font-weight: 700; color: var(--orange); }
  .phone-icon { flex-shrink: 0; display: block; }
  .kennel-mark { position: absolute; left: 367px; top: 682px; width: 150px; text-align: center; line-height: 1; }
  .kennel-mark .kennel-name { font-size: 14px; font-weight: 600; color: var(--white); }
  .kennel-mark .kennel-rule { display: block; margin: 8px auto 6px; width: 120px; height: 2px; background: var(--white); }
  .kennel-mark .kennel-town { font-size: 11px; font-weight: 600; color: var(--white); }
</style>
</head>
<body>
  <main class="poster">
    <div class="hero-photo" role="img" aria-label="Photo of a partridge beside a hunter holding a rifle and a barbed-wire fence post at sunset"></div>

    <h1 class="line brand-name">TALL HERON EXPEDITIONS,</h1>
    <p class="line brand-sub">LLC Millbrook, MO</p>
    <p class="line brand-tag">LICENSED SHOOTING PRESERVE</p>

    <div class="package-banner"></div>
    <h2 class="line banner-title">HUNTING PACKAGES</h2>
    <p class="line banner-sub">½ DAY HUNTS</p>

    <div class="glow-rule" style="top:357px"></div>

    <div class="price-col" style="left:20px"><div class="bird">5 Pheasants</div><div class="price">$120</div></div>
    <div class="col-divider" style="left:186px"></div>
    <div class="price-col" style="left:186px"><div class="bird">7 Chukar</div><div class="price">$125</div></div>
    <div class="col-divider" style="left:352px"></div>
    <div class="price-col" style="left:352px"><div class="bird">8 Quail</div><div class="price">$100</div></div>

    <div class="glow-rule" style="top:444px"></div>
    <p class="line guide-line">Guide Available <span class="amount">$100</span> <span class="unit">per half day</span></p>
    <div class="glow-rule" style="top:487px; opacity:.5"></div>

    <h3 class="line section-title continental">Continental Pheasant Hunt</h3>
    <p class="line minimum">12 Hunter Minimum</p>
    <p class="line fine fine-1">$325 per hunter, includes 12 pheasants per hunter &amp; meal.</p>
    <p class="line fine fine-2">All hunts include bird cleaning Lodging available, call for pricing</p>

    <h3 class="line section-title turkey">Guided Spring Turkey Hunts</h3>
    <p class="line detail detail-1">3 Day Hunt includes meals &amp; lodging $1600</p>
    <p class="line detail detail-2">Guided Whitetail Deer Hunts -Rifle &amp; Archery</p>
    <p class="line detail detail-3">5 Day Hunt includes meals &amp; lodging $2750</p>

    <p class="kennel-note">Training, puppies &amp; started dogs!</p>

    <div class="contact-tag contact-name">
      <svg class="tag-frame" width="121" height="26" viewBox="0 0 121 26"><polygon points="8,1 120,1 113,25 1,25" fill="none" stroke="#EE7325" stroke-width="1.2"/></svg>
      <span>Dale Whitman</span>
    </div>
    <div class="contact-tag contact-phone">
      <svg class="tag-frame" width="168" height="26" viewBox="0 0 168 26"><polygon points="8,1 167,1 160,25 1,25" fill="none" stroke="#FDF4ED" stroke-width="1.2"/></svg>
      <span>
        <svg class="phone-icon" width="14" height="14" viewBox="0 0 24 24" aria-hidden="true"><path fill="#FDF4ED" d="M6.62 10.79c1.44 2.83 3.76 5.14 6.59 6.59l2.2-2.2c.27-.27.67-.36 1.02-.24 1.12.37 2.33.57 3.57.57.55 0 1 .45 1 1V20c0 .55-.45 1-1 1-9.39 0-17-7.61-17-17 0-.55.45-1 1-1h3.5c.55 0 1 .45 1 1 0 1.25.2 2.45.57 3.57.11.35.03.74-.25 1.02l-2.2 2.2z"/></svg>
        555-014-2290
      </span>
    </div>

    <div class="kennel-mark">
      <div class="kennel-name">Pine Hollow Setters</div>
      <span class="kennel-rule"></span>
      <div class="kennel-town">CEDAR BEND, MO</div>
    </div>
  </main>
</body>
</html>
```